" Projetamos espaços internos e externos de ambientes comerciais e residenciais, levando em consideração a funcionalidade do espaço, a estética e o conforto, fazendo do espaço o melhor que ele pode ser. "

```html
<!DOCTYPE html>
<html lang="pt-BR">
<head>
<meta charset="UTF-8">
<title>Marina Teixeira — Design de Ambientes</title>
<link rel="stylesheet" href="https://fonts.googleapis.com/css2?family=Jost:wght@300;400&display=swap">
<style>
  :root {
    --bg: #e9e9e9;
    --card-dark: #0d0d0d;
    --card-light: #ffffff;
    --accent: #e0672b;
    --name-light: #c9c9c9;
  }
  * { margin: 0; padding: 0; box-sizing: border-box; }
  html, body {
    width: 1200px;
    height: 1200px;
    overflow: hidden;
    background: var(--bg);
    font-family: "Jost", sans-serif;
  }
  .stage {
    position: relative;
    width: 1200px;
    height: 1200px;
  }
  .card {
    position: absolute;
    left: 150px;
    width: 900px;
    height: 500px;
    box-shadow: 0 6px 24px rgba(0,0,0,0.12);
  }
  .card--front {
    top: 80px;
    background: var(--card-dark);
    display: flex;
    flex-direction: column;
    align-items: center;
    justify-content: center;
  }
  .brand-name {
    font-weight: 300;
    font-size: 52px;
    letter-spacing: 0.22em;
    color: var(--name-light);
    text-transform: uppercase;
    padding-left: 0.22em;
  }
  .brand-tagline {
    margin-top: 10px;
    font-weight: 400;
    font-size: 17px;
    letter-spacing: 0.5em;
    color: var(--accent);
    text-transform: uppercase;
    padding-left: 0.5em;
  }
  .card--back {
    top: 620px;
    background: var(--card-light);
    color: var(--accent);
    font-weight: 300;
  }
  .contact {
    position: absolute;
    left: 56px;
    top: 52px;
    font-size: 21px;
    line-height: 1.5;
  }
  .contact .phones { margin-top: 22px; }
  .back-name {
    position: absolute;
    left: 0;
    right: 0;
    top: 222px;
    text-align: center;
    font-size: 40px;
    letter-spacing: 0.2em;
    padding-left: 0.2em;
    text-transform: uppercase;
  }
  .social {
    position: absolute;
    right: 56px;
    bottom: 104px;
    display: flex;
    gap: 40px;
  }
  .social-dot {
    width: 30px;
    height: 30px;
    border-radius: 50%;
    background: var(--accent);
  }
  .website {
    position: absolute;
    right: 56px;
    bottom: 48px;
    font-size: 19px;
    letter-spacing: 0.04em;
  }
</style>
</head>
<body>
  <main class="stage">
    <section class="card card--front">
      <div class="brand-name">Marina Teixeira</div>
      <div class="brand-tagline">Design de Ambientes</div>
    </section>

    <section class="card card--back">
      <div class="contact">
        <p class="address">Rua das Acácias, 318 Sala 902<br>Fortaleza - CE</p>
        <p class="phones">+55 11 4021-3376<br>+55 11 4021-3376</p>
      </div>
      <div class="back-name">Marina Teixeira</div>
      <div class="social" aria-label="Redes sociais">
        <span class="social-dot"></span>
        <span class="social-dot"></span>
        <span class="social-dot"></span>
      </div>
      <div class="website">WWW.MARINATEIXEIRA.COM.BR</div>
    </section>
  </main>
</body>
</html>
```